120ml Jar Label — Masculine Cosmetic Foot Balm for Cracked, Hardworking Heels

We need a print-ready wraparound label for a 120ml jar — a brown/amber glass jar with a black metal screw lid (file photo attached).

--DO NOT PUT A BARCODE ON THE LABEL PLEASE--
**PLEASE READ "PLAN HUDDLE PROJECT BRIEF FINAL.MD" IN ATTACHED FILES IF YOU ARE SUBMITTING A DESIGN.**

The label is 190mm wide × 40mm high.
We need files to be in an .ai format with a 2mm bleed at the end.
Social media handle: @bramblekeepnz (facebook, instagram and tiktok)

Bramble Keep is a New Zealand foot-care brand making practical, no-nonsense products for hardworking men whose jobs wreck their feet. Our flagship product, Ridge Mender Balm, helps fix thick, cracked, hardworking skin.

Brand color scheme and overview is all in the brief file. You may add some brand aligned colors outside of the specified hex codes as you see fit to make a great design. Feel free to remove the "Bramble Keep" text from the logo so Bramble Keep is not doubled up on the front of the label

The tone we want: direct, rugged, and credible — like a workwear brand, not a spa brand. Most cracked-heel products on the market lean soft and feminine; we want to stand apart by looking like a serious fix for a real problem, made in New Zealand.

Full legal requirements for New Zealand cosmetic labelling (ingredients, directions, net contents, origin, etc.) are listed in the attached brief document — these are non-negotiable and must stay legible.

Please see the label attached "Label spacing guide" for this project's rough spacing guide. This label is the same size and sits well on the jar. This label doesn't need to be spaced quite as much as the Verin Label

I want to run the design for a week - I feel 7 days is a good amount of time for designers to see the work, digest the brief and create something remarkable and memorable for Bramble Keep.

Target Market(s)

Working men in New Zealand whose jobs or lifestyle put heavy wear on their feet — tradies, farmers, hospital/shift workers, hunters, and outdoors people. Practical, value-driven buyers rather than luxury skincare shoppers.

Industry/Entity Type

Beauty / Health & Wellness / Cosmetics

Font styles to use
Sans Serif
Other font styles liked:
• Montserrat (bold, headings), Inter (regular, body)

Colors
00AB8E
00BBA5
67D7C9
C6EFE9
E9F9F6
FFC000
F8CF3A
FAE287
FDF2CF
FEFAEE

Requirements
Must have
• All NZ cosmetic labelling requirements from the attached brief (product name, tag line, net contents, ingredients, directions, storage, made in NZ) — legible and complete, not omitted for aesthetics Fits 190mm × 40mm wraparound format for a 120ml brown jar with black lid Uses our existing brand colors: Deep Olive #3C4A34, Bone White #F4EFE6, Terracotta Clay #C1683D, and Warm Grey #4A4540 (exact palette in attached brief) Uses Montserrat (headings) and Inter (body) or close equivalents Incorporates our existing shield-and-wing logo (attached) Brand name and product name clearly readable from a normal shelf/bathroom-cabinet distance
Nice to have
• A style that could extend into a hero/product photo later, similar to the NZ-hills-backdrop look on our website (screenshot attached) — not required for the label itself, just good to keep in mind Original icon work (e.g. a small soak/apply/sock icon set) if it fits the rugged brand feel A design that could work as a small back-label/wraparound split if the front can't fit everything at a readable size
Should not have
• No pastel colors, floral motifs, or delicate script fonts — this should never look like spa/luxury skincare. Don't introduce new brand colors outside the palette provided other than black.

```html
<!DOCTYPE html>
<html lang="en">
<head>
<meta charset="utf-8">
<title>Bramble Keep – Ridge Mender Balm wraparound label</title>
<link href="https://fonts.googleapis.com/css2?family=Montserrat:wght@500;700;800&family=Oswald:wght@500;600&display=swap" rel="stylesheet">
<style>
  :root {
    --page-bg: #1e1e1e;
    --olive: #2c4336;
    --clay: #8b5a2f;
    --clay-line: #b36a3a;
    --bone: #f4efe6;
    --cream: #f3e7c8;
    --badge: #9a5d31;
  }
  html, body {
    margin: 0;
    padding: 0;
    width: 1036px;
    height: 1200px;
    overflow: hidden;
    background: var(--page-bg);
  }
  .canvas {
    position: relative;
    width: 1036px;
    height: 1200px;
  }
  .label {
    position: absolute;
    left: 18px;
    top: 494px;
    width: 1000px;
    height: 211px;
    color: var(--bone);
    font-family: "Montserrat", sans-serif;
  }
  .label-bg {
    position: absolute;
    inset: 0;
    width: 1000px;
    height: 211px;
  }
  .block { position: absolute; }

  .directions {
    left: 29px;
    top: 15px;
    width: 245px;
    font-size: 9.4px;
    line-height: 1.3;
    font-weight: 500;
  }
  .directions p { margin: 0 0 7px; }
  .directions strong { font-weight: 700; }

  .brand {
    left: 400px;
    top: 28px;
    width: 110px;
    text-align: center;
  }
  .brand-dot {
    display: block;
    width: 34px;
    height: 34px;
    margin: 0 auto 6px;
    border-radius: 50%;
    background: var(--clay-line);
  }
  .brand-name {
    font-family: "Oswald", sans-serif;
    font-weight: 600;
    font-size: 12.5px;
    letter-spacing: 0.3px;
    line-height: 1;
  }
  .brand-region {
    font-family: "Oswald", sans-serif;
    font-weight: 600;
    font-size: 6px;
    margin-top: 1px;
  }

  .product {
    left: 399px;
    top: 110px;
    width: 235px;
  }
  .product-name {
    margin: 0;
    font-weight: 800;
    font-size: 21px;
    line-height: 0.95;
    color: var(--cream);
    text-transform: uppercase;
  }
  .product-rule {
    height: 1px;
    background: #c99a6e;
    margin: 5px 0 3px;
    width: 170px;
  }
  .tagline {
    font-family: "Oswald", sans-serif;
    font-weight: 500;
    font-size: 11px;
    letter-spacing: 0.4px;
    color: var(--cream);
  }
  .origin {
    margin-top: 8px;
    font-size: 6px;
    font-weight: 700;
  }
  .net {
    left: 572px;
    top: 187px;
    font-size: 10px;
    font-weight: 500;
  }

  .claims {
    left: 29px;
    top: 128px;
    display: flex;
    gap: 20px;
  }
  .claim {
    width: 62px;
    text-align: center;
    font-size: 10px;
    font-weight: 700;
    line-height: 1.1;
  }
  .claim-art {
    display: block;
    width: 34px;
    height: 30px;
    margin: 0 auto 6px;
    border-radius: 8px;
    background: rgba(244, 239, 230, 0.35);
  }
  .claim-art.drop {
    background: none;
    border-radius: 0;
  }

  .features {
    left: 738px;
    top: 16px;
    display: grid;
    grid-template-columns: 125px 110px;
    row-gap: 8px;
  }
  .feature {
    display: flex;
    align-items: center;
    gap: 5px;
    font-size: 9.4px;
    line-height: 1;
    font-weight: 500;
  }
  .feature-badge {
    flex: none;
    width: 34px;
    height: 34px;
    border-radius: 50%;
    background: var(--badge);
    display: flex;
    align-items: center;
    justify-content: center;
  }

  .ingredients {
    left: 738px;
    top: 122px;
    width: 232px;
    font-size: 8.6px;
    line-height: 1.2;
    text-align: justify;
    font-weight: 500;
    margin: 0;
  }
  .ingredients strong { font-weight: 700; }
</style>
</head>
<body>
<div class="canvas">
  <section class="label">
    <svg class="label-bg" viewBox="0 0 1000 211" preserveAspectRatio="none" aria-hidden="true">
      <rect x="0" y="0" width="1000" height="211" fill="var(--olive)"/>
      <path d="M0 104 L40 101 L41 98 L110 102 L180 99 L260 103 L330 100 L400 104 L470 99 L540 102 L600 98 L660 103 L730 100 L800 104 L860 99 L920 101 L960 97 L962 102 L1000 100 L1000 211 L0 211 Z" fill="var(--clay)"/>
      <path d="M7 211 L7 12 Q7 6 13 6 L987 6 Q993 6 993 12 L993 211" fill="none" stroke="var(--clay-line)" stroke-width="2.5"/>
    </svg>

    <div class="block directions">
      <p><strong>Directions:</strong> Apply generously to clean, dry feet, focusing on heels and thick or cracked areas. For cracked heels, wear our moisture-locking socks overnight. Use daily.</p>
      <p><strong>Storage:</strong> Keep out of direct sunlight. Best used within six months of opening.</p>
    </div>

    <div class="block brand">
      <span class="brand-dot"></span>
      <div class="brand-name">BRAMBLE KEEP</div>
      <div class="brand-region">NZ</div>
    </div>

    <div class="block product">
      <h1 class="product-name">Ridge Mender<br>Balm</h1>
      <div class="product-rule"></div>
      <div class="tagline">FOR HARDWORKING SOLES</div>
      <div class="origin">MADE IN NEW ZEALAND</div>
    </div>
    <div class="block net">120mL</div>

    <div class="block claims">
      <div class="claim">
        <span class="claim-art" role="img" aria-label="Icon of two open hands holding a heart"></span>
        hand-made
      </div>
      <div class="claim">
        <svg class="claim-art drop" viewBox="0 0 34 30" aria-hidden="true">
          <path d="M17 2 C12 10 8 15 8 20 a9 9 0 0 0 18 0 C26 15 22 10 17 2 Z" fill="none" stroke="var(--bone)" stroke-width="1.8"/>
        </svg>
        hydrating
      </div>
      <div class="claim">
        <span class="claim-art" role="img" aria-label="Icon of a rabbit"></span>
        not tested on animals
      </div>
    </div>

    <div class="block features">
      <div class="feature">
        <span class="feature-badge" role="img" aria-label="Thick skin icon"></span>
        Thick Skin<br>Formula
      </div>
      <div class="feature">
        <span class="feature-badge">
          <svg width="20" height="20" viewBox="0 0 20 20" aria-hidden="true">
            <rect x="2" y="4" width="16" height="14" rx="2" fill="none" stroke="var(--olive)" stroke-width="1.8"/>
            <line x1="6" y1="2" x2="6" y2="6" stroke="var(--olive)" stroke-width="1.8"/>
            <line x1="14" y1="2" x2="14" y2="6" stroke="var(--olive)" stroke-width="1.8"/>
            <path d="M6 11 L9 14 L14 9" fill="none" stroke="var(--olive)" stroke-width="1.8"/>
          </svg>
        </span>
        Daily Use
      </div>
      <div class="feature">
        <span class="feature-badge" role="img" aria-label="Worker with hard hat icon"></span>
        For Hardworking<br>Feet
      </div>
      <div class="feature">
        <span class="feature-badge" role="img" aria-label="Footprints icon"></span>
        Repairs<br>Cracked Heels
      </div>
    </div>

    <p class="block ingredients"><strong>Ingredients:</strong> Shea Butter, Beef Tallow, Beeswax, Grape Seed Oil, Vegetable Glycerin, Lanolin, Panthenol, Gluconolactone &amp; Sodium Benzoate, Manuka Honey, Allantoin, Vitamin E, Tea Tree Essential Oil, Lemon Myrtle Essential Oil, Rosemary Oleoresin Extract</p>
  </section>
</div>
</body>
</html>
```